Guava Energy Bar Logo and Packaging Art for New Brand/Product

I want to design product packaging for a Guava energy bar that is made primarily from the guava fruit grown on Hawaii. It is a high energy bar designed for quick energy for athletes, hikers, cyclists and adventurers. I want to play in the P.A.E.R and call the bar the "Papaya (prime) Above Every Rival." It will be made from real Guava and wrapped in a compostable leaf wrapper, gluten free and vegan friendly. I want to play on the fact that Guava is a superfood packed with essential vitamins and minerals and free from artificial colours and preservatives.
Target Market(s)
Athletes, Hikers, Cyclists, Runners, Climbers, Triathletes and Adventurers
Requirements
Must have
- I want to make the P.A.E.R. (prime above every rival) woven in the brand and logo with a strong reference to Guava; the super fruit!
Nice to have
- Take a look at the brand and packaging for Tundra Bars

```html
<!DOCTYPE html>
<html lang="en">
<head>
<meta charset="utf-8">
<title>PAER – Papaya Above Every Rival Energy Bar</title>
<link href="https://fonts.googleapis.com/css2?family=Montserrat:wght@900&family=Oswald:wght@300;400&display=swap" rel="stylesheet">
<style>
  :root {
    --sunshine: #fde04f;
    --leaf-green: #7cc08f;
    --leaf-green-soft: rgba(124, 192, 143, 0.85);
    --paper-white: #f4f4f2;
    --berry-pink: #e06fa6;
    --charcoal: #3a3a3a;
    --slate-grey: #6e6e74;
    --frame-grey: #c8c8c8;
  }
  html, body {
    margin: 0;
    padding: 0;
    width: 809px;
    height: 1200px;
    overflow: hidden;
    background: #ffffff;
  }
  .package-face {
    position: relative;
    width: 809px;
    height: 1200px;
    box-sizing: border-box;
    border: 1px solid var(--frame-grey);
    background: var(--sunshine);
    overflow: hidden;
    font-family: "Oswald", "Arial Narrow", sans-serif;
  }
  .brush-stroke,
  .runner-figure {
    position: absolute;
    left: 0;
    top: 0;
  }
  .stack-letter {
    position: absolute;
    left: 50px;
    width: 270px;
    margin: 0;
    font-family: "Montserrat", "Arial Black", sans-serif;
    font-weight: 900;
    font-size: 340px;
    line-height: 1;
    text-align: center;
    color: var(--paper-white);
  }
  .stack-letter--initial {
    top: 25px;
    color: var(--leaf-green-soft);
  }
  .stack-letter--initial-ghost {
    top: 15px;
    left: 40px;
    color: var(--paper-white);
  }
  .stack-letter--a { top: 305px; }
  .stack-letter--e { top: 575px; }
  .stack-letter--r { top: 872px; }
  .brand-name {
    position: absolute;
    left: 300px;
    top: 80px;
    margin: 0;
    font-family: "Montserrat", "Arial Black", sans-serif;
    font-weight: 900;
    color: var(--leaf-green);
    transform: rotate(-12deg);
    transform-origin: left bottom;
    line-height: 1;
  }
  .brand-name__rest {
    display: block;
    font-size: 96px;
    letter-spacing: -1px;
  }
  .brand-name__tagline {
    display: block;
    font-size: 50px;
    margin-top: 6px;
    margin-left: -4px;
    letter-spacing: -0.5px;
  }
  .product-claim {
    position: absolute;
    left: 410px;
    width: 380px;
    margin: 0;
    text-align: center;
  }
  .product-claim--headline {
    top: 522px;
    font-weight: 300;
    font-size: 54px;
    line-height: 1.15;
    color: var(--leaf-green);
  }
  .product-claim--benefit {
    top: 800px;
    font-weight: 300;
    font-size: 34px;
    line-height: 1.2;
    color: var(--slate-grey);
  }
  .claim-divider {
    position: absolute;
    left: 432px;
    top: 907px;
    width: 343px;
    height: 2px;
    background: var(--frame-grey);
  }
  .product-claim--free-from {
    top: 925px;
    font-weight: 300;
    font-size: 27px;
    line-height: 1.2;
    color: var(--slate-grey);
  }
</style>
</head>
<body>
  <main class="package-face">
    <svg class="brush-stroke" width="809" height="1200" viewBox="0 0 809 1200" role="img" aria-label="Pink painted brush stroke sweeping diagonally across the pack">
      <polygon fill="var(--berry-pink)" points="5,648 160,560 320,462 480,372 640,280 790,218 772,246 620,318 470,410 330,505 180,600 15,700"/>
    </svg>

    <p class="stack-letter stack-letter--initial-ghost" aria-hidden="true">P</p>
    <h1 class="stack-letter stack-letter--initial">P</h1>
    <p class="stack-letter stack-letter--a">A</p>
    <p class="stack-letter stack-letter--e">E</p>
    <p class="stack-letter stack-letter--r">R</p>

    <h2 class="brand-name">
      <span class="brand-name__rest">apaya</span>
      <span class="brand-name__tagline">Above Every Rival</span>
    </h2>

    <svg class="runner-figure" width="809" height="1200" viewBox="0 0 809 1200" role="img" aria-label="Silhouette of a runner mid-stride">
      <rect x="250" y="596" width="200" height="494" rx="90" fill="var(--charcoal)"/>
    </svg>

    <p class="product-claim product-claim--headline">The Superfruit<br>Energy Bar!</p>
    <p class="product-claim product-claim--benefit">Packed with Essential<br>Vitamins and Minerals</p>
    <div class="claim-divider"></div>
    <p class="product-claim product-claim--free-from">Free from artificial colours<br>and preservatives</p>
  </main>
</body>
</html>
```